Bramblecups--Wine Bottle Label for Quail Hollowmere

We need a design for a wine bottle labels for 2 custom wines that a local winery is producing for our hunting lodge, Quail Hollowmere. The lodge restaurant is called "Bramblecups", so we'd like to use that as the theme for the label picture. The thought is that we'd use the same design but with different colors for the two types--Red Table Wine and White Table Wine. You can check out our website at www.quailhollowmere.example for inspiration. Since there are many regulations on what goes on the label bottled alcohol in the US, we are just looking for the artwork to be used on the label.

Industry/Entity Type

Hunting

Font styles to use
Decorative
Script

Requirements
Must have
• Bramblecups (as in male US pheasants) should be included in the design.
Nice to have
• It would be nice to have somewhat of an abstract version of a Rooster Pheasant in the design. We would like to see the same design in 2 different color palettes.

```html
<!DOCTYPE html>
<html lang="en">
<head>
<meta charset="utf-8">
<title>Quail Hollowmere – Wine Labels</title>
<link rel="stylesheet" href="https://fonts.googleapis.com/css2?family=Cormorant+SC:wght@500;600&family=Cormorant+Garamond:wght@500&display=swap">
<style>
  :root {
    --page: #ecebe8;
    --paper: #f7f6f2;
    --ink: #1e1c1a;
    --ink-soft: #4a4744;
    --rule: #8d8a86;
    --sketch-a: #d9d8d5;
    --sketch-b: #bdbcb9;
    --white-wine: #e6de2e;
    --white-wine-light: #efe86a;
    --red-wine: #e2312f;
    --red-wine-light: #ea5a55;
  }
  * { box-sizing: border-box; margin: 0; padding: 0; }
  html, body { width: 1200px; height: 1000px; overflow: hidden; }
  body { background: var(--page); }

  .canvas {
    position: relative;
    width: 1200px;
    height: 1000px;
    display: flex;
    justify-content: center;
    align-items: center;
    gap: 120px;
  }

  .label {
    position: relative;
    width: 360px;
    height: 680px;
    background: var(--paper);
    border-radius: 14px;
    overflow: hidden;
    box-shadow: 0 2px 10px rgba(0,0,0,0.08);
  }
  .label--white { --accent: var(--white-wine); --accent-light: var(--white-wine-light); }
  .label--red   { --accent: var(--red-wine);   --accent-light: var(--red-wine-light); }

  .label__base {
    position: absolute;
    inset: 0;
    width: 100%;
    height: 100%;
  }
  .label__base .band { fill: var(--accent); }
  .label__base .band-light { fill: var(--accent-light); }
  .label__base .field { fill: var(--paper); }

  .brand {
    position: absolute;
    top: 48px;
    left: 0;
    right: 0;
    text-align: center;
  }
  .brand__dot {
    display: block;
    width: 30px;
    height: 30px;
    margin: 0 auto 14px;
    border-radius: 50%;
    background: var(--ink);
  }
  .brand__name {
    font-family: "Cormorant SC", serif;
    font-weight: 500;
    font-size: 22px;
    letter-spacing: 1.5px;
    color: var(--ink);
  }
  .brand__rule {
    width: 128px;
    height: 1px;
    margin: 6px auto 0;
    background: var(--rule);
  }

  .pheasant-art {
    position: absolute;
    top: 176px;
    left: 110px;
    width: 150px;
    height: 300px;
    border-radius: 40% 40% 30% 30%;
    background: linear-gradient(180deg, var(--sketch-a), var(--sketch-b) 55%, var(--sketch-a));
    opacity: 0.75;
  }

  .wine-name {
    position: absolute;
    top: 274px;
    left: 0;
    right: 0;
    text-align: center;
    font-family: "Cormorant SC", serif;
    font-weight: 600;
    font-size: 42px;
    line-height: 1.02;
    letter-spacing: 1px;
    color: var(--ink);
  }

  .varietal {
    position: absolute;
    top: 548px;
    left: 0;
    right: 0;
    text-align: center;
    font-family: "Cormorant Garamond", serif;
    font-weight: 500;
    font-size: 19px;
    line-height: 1.75;
    color: var(--ink);
  }
</style>
</head>
<body>
<main class="canvas">

  <article class="label label--white">
    <svg class="label__base" viewBox="0 0 360 680" aria-hidden="true">
      <rect class="band" x="0" y="380" width="360" height="300"/>
      <circle class="band-light" cx="-40" cy="720" r="250"/>
      <circle class="band-light" cx="400" cy="720" r="250"/>
      <circle class="field" cx="180" cy="170" r="340"/>
    </svg>
    <header class="brand">
      <span class="brand__dot"></span>
      <div class="brand__name">Bramblecups</div>
      <div class="brand__rule"></div>
    </header>
    <div class="pheasant-art" role="img" aria-label="Grey line illustration of a standing rooster pheasant"></div>
    <h1 class="wine-name">Quail<br>Hollowmere</h1>
    <p class="varietal">Sauvignon Blanc<br>2016</p>
  </article>

  <article class="label label--red">
    <svg class="label__base" viewBox="0 0 360 680" aria-hidden="true">
      <rect class="band" x="0" y="380" width="360" height="300"/>
      <circle class="band-light" cx="-40" cy="720" r="250"/>
      <circle class="band-light" cx="400" cy="720" r="250"/>
      <circle class="field" cx="180" cy="170" r="340"/>
    </svg>
    <header class="brand">
      <span class="brand__dot"></span>
      <div class="brand__name">Bramblecups</div>
      <div class="brand__rule"></div>
    </header>
    <div class="pheasant-art" role="img" aria-label="Grey line illustration of a standing rooster pheasant"></div>
    <h1 class="wine-name">Quail<br>Hollowmere</h1>
    <p class="varietal">Cabernet Sauvignon<br>2016</p>
  </article>

</main>
</body>
</html>
```